Brantley Advisory Group provides support for renewable energy projects to utilities and suppliers

I need a professional looking business card that is both simple and elegant and unique. My clients are mostly large organizations not individuals. I am a consultant with my own company that is small but would like to give clients the impression I am larger. Smart grid, fiber optics, software, field hardware, distribution automation, substation automation, operations, energy storage/batteries, microgrids, customer service, strategy/roadmaps, conservation, Automated Metering Infrastruture (AMI or smart meters) are all areas of focus.

Target Market(s)

Utilities, suppliers, governmental agencies involved in energy. All types of energy especially natural gas and electrical. Especially renewable energy or green projects.

Contact Information for Business Card

Name - Mark Brantley Cell Phone - 425.318.2746 Email - mbrantley@brantleyag-example.com
Company - Brantley Advisory Group (logo) Title - Principal

Font styles to use
Serif
Sans Serif

Colors

Designer to choose colors to be used in the design.

Requirements
Must have
• Simple and professional and powerful.
• Unique/creative design.
Nice to have
• Utilize color scheme to accent logo colors. Maybe some geometric pattern on edge of card with color.
Should not have
• Busy, complicated, traditional

```html
<!DOCTYPE html>
<html lang="en">
<head>
<meta charset="UTF-8">
<title>Brantley Advisory Group – Business Card</title>
<link href="https://fonts.googleapis.com/css2?family=Arimo:wght@400;700&display=swap" rel="stylesheet">
<style>
  :root {
    --brand-blue: #1d3f94;
    --brand-green: #7a9a52;
    --brand-gray: #999999;
    --card-white: #ffffff;
    --back-gray: #969696;
    --ink: #111111;
    --stage-light: #a6a6a6;
    --stage-dark: #3f3f3f;
  }
  * { margin: 0; padding: 0; box-sizing: border-box; }
  html, body {
    width: 1200px;
    height: 750px;
    overflow: hidden;
  }
  body {
    position: relative;
    background: radial-gradient(ellipse at 35% 40%, var(--stage-light) 0%, #8a8a8a 40%, var(--stage-dark) 100%);
    font-family: "Arimo", Arial, sans-serif;
  }
  .card {
    position: absolute;
    top: 218px;
    width: 492px;
    height: 281px;
    overflow: hidden;
  }
  .card-front { left: 100px; background: var(--card-white); }
  .card-back { left: 601px; background: var(--back-gray); }

  .edge-arcs { position: absolute; inset: 0; width: 492px; height: 281px; }

  .wordmark {
    position: absolute;
    display: flex;
    align-items: center;
    gap: 7px;
    color: var(--brand-blue);
    font-weight: 700;
    white-space: nowrap;
  }
  .wordmark-square {
    display: block;
    background: var(--brand-green);
  }
  .card-front .wordmark {
    right: 20px;
    top: 70px;
    font-size: 16px;
  }
  .card-front .wordmark-square { width: 14px; height: 14px; }

  .person {
    position: absolute;
    right: 20px;
    top: 126px;
    text-align: right;
  }
  .person-name {
    color: var(--brand-blue);
    font-size: 19px;
    font-weight: 700;
    letter-spacing: 0.5px;
    line-height: 22px;
  }
  .person-title {
    color: var(--ink);
    font-size: 16px;
    line-height: 19px;
    padding-bottom: 3px;
    border-bottom: 2px solid var(--brand-blue);
    display: inline-block;
    min-width: 100px;
  }

  .contact-list {
    position: absolute;
    right: 20px;
    top: 178px;
    list-style: none;
  }
  .contact-item {
    display: flex;
    justify-content: flex-end;
    align-items: center;
    gap: 10px;
    height: 20.5px;
    font-size: 13.5px;
    color: var(--ink);
  }
  .contact-icon {
    width: 17px;
    height: 17px;
    flex: none;
  }

  .back-band {
    position: absolute;
    left: 1px;
    right: 1px;
    top: 77px;
    height: 118px;
    background: var(--card-white);
    border: 4px solid var(--brand-blue);
  }
  .card-back .wordmark {
    left: 50%;
    top: 50%;
    transform: translate(-50%, -50%);
    font-size: 24px;
    gap: 10px;
  }
  .card-back .wordmark-square { width: 20px; height: 20px; }
</style>
</head>
<body>

  <section class="card card-front" aria-label="Business card front">
    <svg class="edge-arcs" viewBox="0 0 525 300" preserveAspectRatio="none" aria-hidden="true">
      <circle cx="43" cy="107" r="195" fill="var(--brand-gray)"/>
      <circle cx="20" cy="135" r="193" fill="var(--card-white)"/>
      <circle cx="20" cy="135" r="191" fill="var(--brand-green)"/>
      <circle cx="-4.6" cy="150" r="193" fill="var(--card-white)"/>
      <circle cx="-4.6" cy="150" r="190.6" fill="var(--brand-blue)"/>
    </svg>

    <div class="wordmark">
      <span class="wordmark-square"></span>
      <span class="wordmark-name">Brantley Advisory Group</span>
    </div>

    <div class="person">
      <p class="person-name">Mark Brantley</p>
      <p class="person-title">(Owner)</p>
    </div>

    <ul class="contact-list">
      <li class="contact-item">
        <span>425.318.2746</span>
        <svg class="contact-icon" viewBox="0 0 20 20" aria-label="Phone">
          <circle cx="10" cy="10" r="10" fill="var(--brand-green)"/>
          <path d="M6.5 5.2c.5-.4 1.1-.3 1.4.2l.9 1.5c.3.5.2 1-.2 1.3l-.6.5c.5 1.2 1.5 2.3 2.8 2.9l.5-.6c.3-.4.9-.5 1.3-.2l1.5.9c.5.3.6.9.2 1.4l-.6.7c-.6.6-1.6.8-2.4.4-2.4-1.1-4.3-3-5.3-5.4-.3-.8-.1-1.7.5-2.3z" fill="#fff"/>
        </svg>
      </li>
      <li class="contact-item">
        <span>mbrantley@brantleyag-example.com</span>
        <svg class="contact-icon" viewBox="0 0 20 20" aria-label="Email">
          <circle cx="10" cy="10" r="10" fill="var(--brand-green)"/>
          <rect x="5" y="6.5" width="10" height="7" rx="0.8" fill="#fff"/>
          <path d="M5.3 7l4.7 3.6L14.7 7" fill="none" stroke="var(--brand-green)" stroke-width="1"/>
        </svg>
      </li>
      <li class="contact-item">
        <span>www.brantleyag-example.com</span>
        <svg class="contact-icon" viewBox="0 0 20 20" aria-label="Website">
          <circle cx="10" cy="10" r="10" fill="var(--brand-green)"/>
          <circle cx="10" cy="10" r="5.2" fill="none" stroke="#fff" stroke-width="1.3"/>
          <ellipse cx="10" cy="10" rx="2.2" ry="5.2" fill="none" stroke="#fff" stroke-width="1"/>
          <path d="M4.8 10h10.4" stroke="#fff" stroke-width="1"/>
        </svg>
      </li>
    </ul>
  </section>

  <section class="card card-back" aria-label="Business card back">
    <div class="back-band">
      <div class="wordmark">
        <span class="wordmark-square"></span>
        <span class="wordmark-name">Brantley Advisory Group</span>
      </div>
    </div>
  </section>

</body>
</html>
```